Re jig a A4 Instructional Flyer

We need an established A4 instructional Flyer (2 pages x A4) - to be rejigged in Harcourt College of Learning Branding to look fresh and new.

Permissions have been received to rejig this Medical Triage Chart. Fresh branding and setting out (fonts) required.

FOOTER NOTES : to be inserted at the bottom of the A4 instruction sheet

Harcourt College produced with permissions from Outback Care Alliance, produced by Outback Care Alliance with Clinic Circle Uptown with permissions from Southern Lakes Carewell Hub. Harcourt acknowledges the NBFPS Standards Criterion 3.2.3 Practice Training and Education in Triage

Target Market(s)

Medical Practices

Industry/Entity Type

Health

Font styles to use
Serif

Colors
0255a3
f78f20

Requirements
Must have
• Professional
• Pops of colour in the chart.
• This chart is to be USED and is VISUAL (no boring grey words throughout)
• PROBS SANS SERIF but SERIF for titles OK
Nice to have
• look at www.harcourtlearn.edu.au FOR BRANDING look and feel

```html
<!DOCTYPE html>
<html lang="en">
<head>
<meta charset="utf-8">
<title>Triage – Harcourt College of Learning</title>
<link href="https://fonts.googleapis.com/css2?family=Cormorant+Garamond:wght@500;600&family=Jost:ital,wght@0,400;0,500;0,600;1,500&display=swap" rel="stylesheet">
<style>
:root{
  --orange:#f78f20;
  --blue:#0255a3;
  --navy:#0b3f6b;
  --ink:#1a1a1a;
  --grey:#8a8a8a;
  --red:#e8322f;
  --green:#1f9e4a;
  --cat1:#e8322f;
  --cat2:#f26522;
  --cat3:#f2bb12;
  --cat4:#17a880;
  --cat5:#5b1f8f;
  --cat6:#1b9ad6;
  --serif:"Cormorant Garamond",Georgia,serif;
  --sans:"Jost",Arial,sans-serif;
}
*{box-sizing:border-box;margin:0;padding:0}
html,body{width:1200px;height:846px;overflow:hidden;background:#fff}
body{position:relative;font-family:var(--sans);color:var(--ink)}
.abs{position:absolute}
p,li{line-height:1.3}

/* headers */
.page-header{position:absolute;background:var(--orange);color:#fff;display:flex;align-items:center}
.page-header h1{font-family:var(--serif);font-weight:500;font-variant:small-caps;letter-spacing:.5px;line-height:1}
.page-header .divider{width:1px;background:#fff;align-self:center}
.page-header .tagline{font-family:var(--serif);font-size:9.5px;font-weight:500}

/* flow chart */
.flow-box{position:absolute;border:1.5px solid var(--green);font-size:6.3px;font-weight:500;text-align:center;display:flex;flex-direction:column;justify-content:center;background:#fff;line-height:1.2}
.pill{position:absolute;border:1.5px solid;border-radius:9px;font-size:7px;font-weight:600;display:flex;align-items:center;justify-content:center;background:#fff}
.pill.yes,.pill.no{border-color:var(--red)}
.pill.unsure{border-color:var(--blue);font-size:6.3px}
.info-box{position:absolute;border:1.5px solid;padding:5px 5px;font-size:5.2px;background:#fff}
.info-box h3{font-size:6.5px;font-weight:600;margin-bottom:3px;text-align:center;line-height:1.2}
.info-box ul{list-style:none}
.info-box li{margin-bottom:1.2px;line-height:1.25}
.record{border-color:var(--orange)}
.plan{border-color:var(--red)}
.plan h3{color:var(--red);font-size:7.5px;text-align:left}
.plan .call{color:var(--red);font-weight:600;text-align:center;font-size:8px;margin-top:3px;line-height:1.1}
.plan .call small{display:block;font-size:6px}
.brand-box{position:absolute;border:1.5px solid var(--navy);display:flex;flex-direction:column;align-items:center;justify-content:center;gap:6px;text-align:center;background:#fff}
.brand-mark{background:var(--navy)}
.brand-name{font-family:var(--serif);font-weight:600;color:var(--navy);line-height:1.1}

.banner{position:absolute;background:var(--navy);color:#fff;border-radius:8px;font-size:8.2px;letter-spacing:.9px;font-weight:500;display:flex;align-items:center;justify-content:center}

/* category table + footer stack */
.chart-stack{position:absolute;display:flex;flex-direction:column;gap:7px}
.cat-table{border-collapse:collapse;table-layout:fixed;width:100%;font-size:4.8px}
.cat-table th{color:#fff;font-size:8px;font-weight:500;height:14px;line-height:1}
.cat-table td{border:.6px solid #9a9a9a;vertical-align:top;padding:2px 3px;line-height:1.22}
.cat-table tr.symptoms td{height:66px}
.cat-table tr.tell td{height:24px;text-align:center;vertical-align:middle;font-size:5.3px}
.cat-table tr.tell td:first-child{font-size:6.5px}
.cat-table tr.action td{height:25px;text-align:center;vertical-align:middle;font-size:5.3px}
.cat-table tr.action b{color:var(--red);font-weight:600}
.cat-table tr.retrieve td{height:20px;text-align:center;vertical-align:middle;font-size:4.2px;font-weight:600;white-space:nowrap;overflow:hidden;padding:0 2px}
.c1{background:var(--cat1)}.c2{background:var(--cat2)}.c3{background:var(--cat3)}
.c4{background:var(--cat4)}.c5{background:var(--cat5)}.c6{background:var(--cat6)}
.footnote{font-size:3.9px;font-weight:500;text-align:center;line-height:1.4}
.footnote.abs{position:absolute}

/* right page */
.col h2{font-size:9.5px;font-weight:500;line-height:1.1;margin-bottom:8px;color:#222}
.col p{font-size:4.9px;margin-bottom:5px}
.col ol{list-style:none;font-size:4.9px}
.col ol li{margin-bottom:5px}
.cat-note{font-size:4.9px;margin-bottom:6px}
.cat-note b{font-weight:600}
.t1{color:var(--cat1)}.t2{color:var(--cat2)}.t3{color:var(--cat3)}
.t4{color:var(--cat4)}.t5{color:var(--cat5)}.t6{color:var(--cat6)}
.plan-lg{position:absolute;border:1.8px solid var(--red);padding:5px 8px}
.plan-lg h3{color:var(--red);font-size:11px;font-weight:500;margin-bottom:3px;line-height:1.1}
.plan-lg ul{list-style:none;font-size:5px;padding-left:6px}
.plan-lg li{margin-bottom:2px}
.plan-lg .call{color:var(--red);text-align:center;font-weight:600;font-size:10px;line-height:1.1;margin-top:3px}
.plan-lg .call small{display:block;font-size:7.5px}
.record-note{position:absolute;font-style:italic;font-weight:500;color:var(--grey);font-size:6.6px;text-align:center;line-height:1.55;letter-spacing:.2px}
</style>
</head>
<body>

<!-- ============ PAGE 1 : TRIAGE ============ -->
<header class="page-header" style="left:38px;top:212px;width:559px;height:56px;padding-left:20px">
  <h1 style="font-size:27px">Triage</h1>
  <span class="divider" style="height:24px;margin:0 14px"></span>
  <span class="tagline">a guide to urgency for non-clinical staff in general practice for telephone and walk in presentations</span>
</header>

<div class="flow-box" style="left:56px;top:285px;width:110px;height:18px">Do you have an urgent problem?</div>
<svg class="abs" style="left:166px;top:286px" width="58" height="100" viewBox="0 0 58 100" aria-hidden="true">
  <polygon points="2,5 8,5 8,1 14,9 8,17 8,13 2,13" fill="#111"/>
  <polygon points="2,77 8,77 8,73 14,81 8,89 8,85 2,85" fill="#111"/>
  <polygon points="50,5 53,5 53,1 58,9 53,17 53,13 50,13" fill="#111"/>
  <polygon points="50,77 53,77 53,73 58,81 53,89 53,85 50,85" fill="#111"/>
</svg>
<div class="pill yes" style="left:184px;top:287px;width:34px;height:16px">YES</div>
<svg class="abs" style="left:101px;top:304px" width="20" height="50" viewBox="0 0 20 50" aria-hidden="true">
  <polygon points="6,0 14,0 14,6 19,6 10,13 1,6 6,6" fill="#111"/>
  <polygon points="6,32 14,32 14,38 19,38 10,45 1,38 6,38" fill="#111"/>
</svg>
<div class="pill unsure" style="left:73px;top:319px;width:76px;height:16px">NO / I DON'T KNOW</div>
<div class="flow-box" style="left:56px;top:351px;width:110px;height:30px">The next available appointment is<br>. . .<br>Is this ok?</div>
<div class="pill no" style="left:184px;top:358px;width:34px;height:16px">NO</div>

<div class="info-box record" style="left:229px;top:285px;width:118px;height:97px">
  <h3>RECORD THE PATIENT'S<br>PHONE NUMBER</h3>
  <ul>
    <li>• What is the name and age of the patient?</li>
    <li>• What is the nature of the problem?</li>
    <li>• What is the duration of the problem?</li>
    <li>• What is the severity of the problem?</li>
    <li>• Has the patient had any previous<br>&nbsp;&nbsp;major health problems?</li>
    <li>• Select a category below<br>&nbsp;&nbsp;and follow instructions.</li>
  </ul>
</div>

<div class="info-box plan" style="left:352px;top:285px;width:118px;height:97px">
  <h3>EMERGENCY ACTION PLAN</h3>
  <ul>
    <li>• Remain calm and do not panic.</li>
    <li>• Be aware and respond to the<br>&nbsp;&nbsp;needs of the emergency.</li>
    <li>• Assess which patient needs<br>&nbsp;&nbsp;to take priority.</li>
    <li>• Deal with any injury or illness in<br>&nbsp;&nbsp;order of severity.</li>
  </ul>
  <p class="call">CALL 9-1-1<small>FOR AMBULANCE, POLICE OR FIRE</small></p>
</div>

<div class="brand-box" style="left:475px;top:285px;width:105px;height:97px">
  <span class="brand-mark" style="width:14px;height:14px"></span>
  <span class="brand-name" style="font-size:11px">HARCOURT COLLEGE<br>OF LEARNING</span>
</div>

<div class="banner" style="left:51px;top:401px;width:534px;height:14px">PRACTICE TO ASK THE PATIENT OR CALLER TO DESCRIBE THE PROBLEM(S) AND CATEGORISE ACCORDINGLY</div>

<div class="chart-stack" style="left:51px;top:429px;width:535px">
<table class="cat-table">
  <tr>
    <th class="c1">CATEGORY 1</th><th class="c2">CATEGORY 2</th><th class="c3">CATEGORY 3</th>
    <th class="c4">CATEGORY 4</th><th class="c5">CATEGORY 5</th><th class="c6">CATEGORY 6</th>
  </tr>
  <tr class="symptoms">
    <td>• Chest pain<br>• Breathing difficulties/trouble talking<br>• Facial swelling and rash<br>• Collapse/altered consciousness<br>• Facial/limb weakness<br>• Extensive burns<br>• Sick patient you have concerns about</td>
    <td>• Fitting<br>• Bleeding (heavy or persistent)<br>• Spinal or head injury/trauma<br>• Snake bite<br>• Heart palpitations<br>• In labour/ruptured membranes<br>• Neck stiffness/altered consciousness</td>
    <td>• Unable to urinate<br>• Unwell 'floppy' infant<br>• Poisoning/overdose<br>• Eye injuries/chemical in the eye<br>• Pain (severe)<br>• Injured limb/possible fracture</td>
    <td>• Unwell child/elder with fever, vomiting, diarrhoea or pain for &gt; 24 hours<br>• Pregnancy: pain or bleeding, reduced foetal movement<br>• Abuse or assault<br>• Visual disturbance<br>• Patient or carer with extreme concern<br>• Psychological distress</td>
    <td>• Unwell child/elderly with fever, vomiting, diarrhoea or pain for &lt;24 hours<br>• Rash (severe)<br>• Cut/laceration<br>• Severe flu like symptoms</td>
    <td>• Adult with fever, but otherwise well<br>• Post op problems<br>• Eye or ear infections/pain<br>• Adult with continuous vomiting and/or diarrhoea for &gt;24 hrs</td>
  </tr>
  <tr class="tell">
    <td>tell Caller to Call <b>9-1-1</b></td>
    <td>tell caller to go to the<br>EMERGENCY DEPT NOW</td>
    <td>tell caller to put call through<br>to Nurse or Doctor</td>
    <td>tell caller come to surgery now<br>advise the on-call Nurse or Doctor</td>
    <td>tell caller come to surgery<br>advise the on-call Nurse or Doctor</td>
    <td>tell caller to make an appointment within 24 hrs &amp; call back if symptoms get worse</td>
  </tr>
  <tr class="action">
    <td><b>ACTION:</b> Call Nurse or Doctor<br>for help immediately</td>
    <td><b>ACTION:</b> Interrupt Nurse<br>or Doctor immediately</td>
    <td><b>ACTION:</b><br>Advise Nurse or Doctor now.</td>
    <td><b>ACTION:</b><br>Discuss with Nurse or Doctor</td>
    <td><b>ACTION:</b><br>Notify Nurse or Doctor &lt; 30 min</td>
    <td><b>ACTION:</b><br>Notify Nurse or Doctor.</td>
  </tr>
  <tr class="retrieve">
    <td>Retrieve patient file Document activity</td><td>Retrieve patient file Document activity</td>
    <td>Retrieve patient file Document activity</td><td>Retrieve patient file Document activity</td>
    <td>Retrieve patient file Document activity</td><td>Retrieve patient file Document activity</td>
  </tr>
</table>

<p class="footnote">Harcourt College produced with permissions from Outback Care Alliance, produced by Outback Care Alliance with Clinic Circle Uptown with permissions from Southern Lakes Carewell Hub. Harcourt acknowledges the NBFPS Standards Criterion 3.2.3 Practice Training and Education in Triage</p>
</div>

<!-- ============ PAGE 2 : FRONT DESK TRIAGE ============ -->
<header class="page-header" style="left:611px;top:212px;width:559px;height:61px;padding-left:101px">
  <h1 style="font-size:24px">Front Desk Triage</h1>
  <span class="divider" style="height:24px;margin:0 12px"></span>
  <span class="tagline">How to manage common scenarios faced by reception staff</span>
</header>
<div class="brand-box" style="left:624px;top:224px;width:67px;height:60px;gap:4px">
  <span class="brand-mark" style="width:9px;height:9px"></span>
  <span class="brand-name" style="font-size:6.5px">HARCOURT COLLEGE<br>OF LEARNING</span>
</div>

<section class="col abs" style="left:630px;top:290px;width:160px">
  <h2>IS THIS AN EMERGENCY?</h2>
  <p>• When answering the telephone, all callers should be asked if the matter is an emergency prior to being placed on hold. Ask the patient, "Is this an emergency or can I place you on hold for a moment?"</p>
  <p>• Consider the TRIAGE STEPS and CATEGORIES listed on the reverse of this document to assess the patient's status.</p>
  <h2 style="margin-top:12px">ASK THE PATIENT – TRIAGE STEPS</h2>
  <ol>
    <li>1. Confirm the patient's name and phone number.</li>
    <li>2. Does the patient attend the surgery?<br>(ie. Does the practice have previous medical records to hand?)</li>
    <li>3. Location.<br>("Are you at home?" "Are you alone?")</li>
    <li>4. Nature of their problem.<br>(Patient may prefer to speak to the practice nurse or on call doctor.)</li>
    <li>5. Duration of their symptoms.<br>("How long have you felt like this?")</li>
    <li>6. Severity of their problem.<br>("On a scale of 1 to 10 how severe is the pain?" [if applicable].)</li>
    <li>7. Any previous major health problems.<br>("Are you on any medication?" "Do you have any allergies?")</li>
  </ol>
</section>

<div class="plan-lg" style="left:624px;top:518px;width:166px;height:80px">
  <h3>EMERGENCY ACTION PLAN</h3>
  <ul>
    <li>• Remain calm and do not panic.</li>
    <li>• Be aware and respond to the needs of the emergency.</li>
    <li>• Assess which patient needs to take priority.</li>
    <li>• Deal with any injury or illness in order of severity.</li>
  </ul>
  <p class="call">CALL 9-1-1<small>FOR AMBULANCE, POLICE OR FIRE</small></p>
</div>

<section class="col abs" style="left:807px;top:287px;width:165px">
  <h2>ON THE DAY<br>EMERGENCIES IN THE CLINIC</h2>
  <p class="cat-note"><b class="t1">CATEGORY 1</b> patients should immediately be seen by the on-call doctor or other medical professional on duty.</p>
  <p class="cat-note"><b class="t2">CATEGORY 2</b> patients should be directed to the emergency department of their nearest hospital.</p>
  <p class="cat-note"><b class="t3">CATEGORY 3</b> patients or patients with worsening symptoms should be referred to the practice nurse or on call doctor.</p>
  <p class="cat-note"><b class="t4">CATEGORY 4</b> patients should be advised to attend the clinic immediately and triaged by the practice nurse (may then be slotted in between appointments or at the end of the session).</p>
  <p class="cat-note"><b class="t5">CATEGORY 5</b> patients should make an appointment for the day and be advised to call back if symptoms worsen.</p>
  <p class="cat-note"><b class="t6">CATEGORY 6</b> patients should make an appointment within 24 hours and call back if symptoms worsen.</p>
  <h2 style="margin-top:16px">PATIENTS PRESENTING WITH SYMPTOMS OF POTENTIAL COMMUNICABLE DISEASES</h2>
  <p>• Such as 'influenza'(flu), measles, chicken pox should be isolated to a secluded area of the medical practice such as the nurses' office. Where possible, a notice of isolation is to be fixed to the door to limit access in this area.</p>
  <p>• Patients with 'flu like symptoms should be required to wear a surgical mask.</p>
  <p>• If the patient is bleeding or vomiting, put gloves on before you assist them.</p>
</section>

<section class="col abs" style="left:990px;top:290px;width:165px">
  <h2>SCHEDULING CARE</h2>
  <p>• Reception staff should reserve several unbooked appointment times each day for 'on the day' urgent appointments such as unwell children and the elderly, lacerations and suspected fractures.</p>
  <p>• If your practice does not operate on an appointment system, patients should be triaged on walk in and advised of the expected waiting time to see the doctor, nurse or Aboriginal health worker.</p>
  <p>• Where a patient is assessed as in need of urgent medical attention over the telephone, advise the caller to hang up and call <b>9-1-1</b> immediately for an ambulance.</p>
  <p>• Where a receptionist is unable to determine the urgency of a telephone call, the patient should be transferred to the practice nurse or on-call doctor for triage.</p>
  <p>• If a patient presents in person and requires urgent medical assistance after the doctor has left – call <b>9-1-1</b> for ambulance.</p>
  <p>• Clinical staff treating the patient should wear as a minimum, a surgical mask, gloves and when collecting nose and/or throat swabs, protective eyewear.</p>
</section>

<p class="record-note" style="left:985px;top:497px;width:172px">ALL EMERGENCY CASES DEALT WITH BY RECEPTION SHOULD BE RECORDED BY THE STAFF MEMBER INVOLVED IN THE PATIENT HEALTH RECORD IN ADDITION TO THE CLINICAL NOTES RECORDED BY THE PRACTICE NURSE OR DOCTOR/S TREATING THE PATIENT.</p>

<p class="footnote abs" style="left:807px;top:584px;width:350px;text-align:left">Harcourt College produced with permissions from Outback Care Alliance, produced by Outback Care Alliance with Clinic Circle Uptown with permissions from Southern Lakes Carewell Hub.<br>Harcourt acknowledges the NBFPS Standards Criterion 3.2.3 Practice Training and Education in Triage</p>

</body>
</html>
```